Creative Brochure for Beauty School

We need a brochure designed on legal sized paper (8.5" X 14"), folded in half, and stapled in the middle, to create an 8-page (including covers) project. Therefore, your design for each page should be prepared in 7"x8.5" size (vertical). The brochure should have the look and feel of a magazine (a couple of samples attached to brief files for your reference). Think a magazine published for individuals interested in becoming beauty and wellness professionals. GET CREATIVE! We give you complete creative freedom.

NOTE: FOR DESIGN SELECTION PURPOSES, WE ONLY REQUIRE THE COVER AND 1-2 PAGES. I DO NOT NEED THE COMPLETED BROCHURE, AS I REALIZE TIME IS MONEY. WE WILL WORK TOGETHER TO COMPLETE PROJECT ONCE A DESIGN IS SELECTED.

Our school has been in business for over a decade and provides education in beauty and wellness programs. The purpose of this brochure is to showcase all our program offerings to prospect students in a creative and inspiring way. The brochure will be provided to everyone that inquires about our programs of study and it should provide basic and straightforward information about the school and each program, along with notable facts about us or the industry.

The design should consist of the following elements:

1. Front Cover page. Needs to be beautifully designed and eye catching, having the look and feel of a magazine cover. Cover must have:

- Logo: used as the "magazine’s" masthead
- Tag Line::::::: Beautify your future
-main image (use any of the attached images OR any stock image that can be purchased later by us). Only requirement is that the image has to be of stunning quality.
-Cover lines: (Designers, you may show your creativity). Some ideas on cover lines:
+8 beauty and wellness programs ::::: Endless career opportunities
+Academic Excellence: 82.44% graduation rate in 2012-2013^^
+Affordable tuition and financial assistance programs available.*
+ Miami’s premier choice for beauty education

-any other element desired to enhance the magazine theme.

-Required Disclaimer: (required disclaimers but can and should be very small print)

^^Based on TRELVIN’ 2012-13 Annual Report
*Financial aid available to those who qualify.

2. Must dedicate an area for each of our programs of study. We offer 8 programs, but some can be combined into one page in the layout. The programs can be divided into 2 main categories: beauty programs and spa/wellness programs. The content for each program will be provided later, depending on the design, but we do not expect it to exceed 3-4 sentences of main text for each program. The layout should be easy to read through use of typography, headlines, pull quotes, font colors and hierarchy. The copy should not be lengthy, rather concise and easy to read.

***The beauty programs are:
-Cosmetology (this is the main program so give it the importance it merits in the design)
-Makeup Artistry
-Barber (mainly designed for male students, if images are used, they should be male model)

***Spa/Wellness programs:
-Spa Therapy
-Massage Therapy (can showcase a photo of a male if needed to create diversity)
-Skin Care
-Manicure, Pedicure & Nail Extensions
-Full Specialist (combines the Skin Care and Manicure, Pedicure & Nail Extensions programs)

FYI: Please use the names of the programs verbatim.

3. Areas for (brief) industry content, testimonials (which can include a picture of the individual, to be provided later, should the design require it), facts about the school or industry, and any other idea you come up with.

4. Back cover. Allow area for mailing.

I have added several photos to this brief that you may use as you wish, although some may need Photoshopping. Please use any other photo you want, as long as you have copyrights or if we can buy the rights to the image later. Also added to files, photo of business card and screenshot of website design (no published yet) for color reference.

**This design will require 2 language versions, one in English and one in Spanish. Once a design is selected, we will provide all the necessary text in English and Spanish to allow you to complete.
Updates

Hello everyone:

I have added to the design brief a Microsoft word document with all the (English) text that we need to add to the brochure. I will really appreciate it if you go ahead and prepare a couple of these pages, to match the look and feel of the front cover, using the text and specifications provided in that document. I give you complete freedom in designing the body of the brochure. You may re-arrange the text, as long as you use everything or manage to convey the same message. If you feel that something in the text can be said differently, let me know, or present it. The text is not set in stone, we are open to your creative ideas.

Thanks-

Target Market(s)

Adults 18-49 years, typically our student body in comprised of 70% female / 30% male. The look should be modern, hip yet elegant and sophisticated.

Industry/Entity Type

Education

Requirements
Must have
• Magazine look and feel. Beautiful, eye catching design. We sell beauty, therefore design should be beautiful and glamorous, to go along with the industry.

-include tag line: Beautify your future
-Contact info:
Address: 5312 NW 4th Avenue. Miami, Fl 33052
Tel: 305-491-5836
Fax: 786-552-9274
www.marlowvista.edu
Instagram & Facebook icons / marlowvistabeautyschool
Should not have
• Should not have a corporate/serious feel or boring look.

```html
<!DOCTYPE html>
<html lang="en">
<head>
<meta charset="utf-8">
<title>Marlow Vista School of Beauty — Cover</title>
<link rel="stylesheet" href="https://fonts.googleapis.com/css2?family=Inter:wght@200;300;400;600;700&display=swap">
<style>
  :root {
    --backdrop: #e6e4e2;
    --paper: #ffffff;
    --magenta: #d81b5a;
    --magenta-band: #e0467a;
    --ink: #2a2a2a;
    --ink-soft: #3a3a3a;
    --ink-muted: #6f6760;
    --skin-light: #f6e6da;
    --skin-mid: #e9c3ac;
    --hair: #efe2c8;
    --hair-red: #c9405f;
  }
  * { margin: 0; padding: 0; box-sizing: border-box; }
  html, body {
    width: 1200px; height: 1200px; overflow: hidden;
    background: var(--backdrop);
    font-family: "Inter", Helvetica, Arial, sans-serif;
  }
  .cover {
    position: absolute; left: 147px; top: 50px;
    width: 906px; height: 1100px;
    background: var(--paper);
    overflow: hidden;
    box-shadow: 0 6px 24px rgba(0,0,0,.18);
  }
  .cover-photo {
    position: absolute; left: 43px; top: 51px; right: 0; bottom: 0;
    background:
      radial-gradient(ellipse 36% 32% at 42% 46%, var(--skin-mid) 0%, var(--skin-light) 55%, transparent 100%),
      radial-gradient(ellipse 40% 40% at 75% 40%, var(--hair) 0%, transparent 70%),
      radial-gradient(ellipse 20% 60% at 0% 70%, var(--hair-red) 0%, transparent 80%),
      linear-gradient(180deg, #f7f1ec 0%, #fbf7f3 60%, #f6ece4 100%);
  }
  .spine-band {
    position: absolute; left: 0; top: 0; bottom: 0; width: 43px;
    background: linear-gradient(180deg, var(--magenta-band), #d93b71);
  }
  .issue-date {
    position: absolute; left: 21px; top: 175px;
    transform: translate(-50%, -50%) rotate(-90deg);
    white-space: nowrap;
    color: #fff; font-size: 13px; font-weight: 400; letter-spacing: 2px;
  }
  .tagline-strip {
    position: absolute; left: 43px; top: 0; right: 0; height: 51px;
    background: var(--paper);
  }
  .tagline {
    position: absolute; left: 140px; top: 14px; width: 660px;
    text-align: center; color: var(--magenta);
    font-size: 26px; font-weight: 300; letter-spacing: 13.5px;
  }
  .masthead-name {
    position: absolute; left: 140px; top: 62px; width: 680px;
    text-align: center; white-space: nowrap;
    color: var(--ink); font-weight: 700;
    font-size: 100px; line-height: 1; letter-spacing: -3px;
  }
  .masthead-sub {
    position: absolute; left: 300px; top: 200px; width: 440px;
    text-align: center; white-space: nowrap;
    color: var(--ink); font-weight: 700;
    font-size: 34px; line-height: 1; letter-spacing: 0.5px;
  }
  .mark {
    display: inline-block; position: relative;
    width: 60px; height: 1em; vertical-align: baseline;
  }
  .mark svg {
    position: absolute; left: 0; top: -0.35em;
    width: 54px; height: 58px;
  }
  .coverline { position: absolute; color: var(--ink); }
  .coverline.right { right: 20px; text-align: right; }
  .headline { font-weight: 200; font-size: 57px; line-height: 64px; letter-spacing: -1.5px; white-space: nowrap; }
  .deck { font-weight: 300; font-size: 28px; line-height: 36px; letter-spacing: 2px; color: var(--ink-soft); }
  .figure { font-weight: 200; font-size: 86px; line-height: 88px; letter-spacing: -1px; }
  .figure-note { font-weight: 700; font-size: 15.5px; margin-top: 4px; }
  .soft { font-weight: 200; font-size: 30px; line-height: 38px; color: var(--ink-muted); letter-spacing: -0.3px; white-space: nowrap; }
  .coverline.left .lead-mark {
    position: absolute; left: -60px; top: -6px; width: 54px; height: 58px;
  }
</style>
</head>
<body>
  <article class="cover">
    <div class="cover-photo" role="img" aria-label="Cover photo: close-up beauty portrait of a blonde model with smoky plum eye makeup, glossy pink lips and long black beaded earrings"></div>

    <div class="spine-band"><span class="issue-date">| 01 JANUARY 2014 |</span></div>

    <div class="tagline-strip"></div>
    <p class="tagline">BEAUTIFY YOUR FUTURE</p>

    <h1>
      <span class="masthead-name">Marlow Vista</span>
      <span class="masthead-sub">SCHOOL OF BEAUTY</span>
    </h1>

    <div class="coverline right" style="top:316px">
      <p class="headline"><span class="mark"><svg viewBox="0 0 60 64" aria-hidden="true"><path d="M22 2 L32 2 L30 26 L58 23 L58 32 L30 34 L28 62 L19 60 L21 34 L2 35 L3 27 L22 25 Z" fill="var(--magenta)"/></svg></span>8 beauty<br>&amp; wellness<br>programs:</p>
      <p class="deck" style="margin-top:10px">Endless career<br>opportunities</p>
    </div>

    <div class="coverline right" style="top:634px">
      <p class="headline"><span class="mark"><svg viewBox="0 0 60 64" aria-hidden="true"><path d="M22 2 L32 2 L30 26 L58 23 L58 32 L30 34 L28 62 L19 60 L21 34 L2 35 L3 27 L22 25 Z" fill="var(--magenta)"/></svg></span>Academic<br>Excellence:</p>
      <p class="figure">82.44%</p>
      <p class="figure-note">graduation rate in 2012-2013*</p>
    </div>

    <div class="coverline right" style="top:906px">
      <p class="soft"><span class="mark" style="width:56px"><svg viewBox="0 0 60 64" aria-hidden="true" style="top:-0.6em"><path d="M22 2 L32 2 L30 26 L58 23 L58 32 L30 34 L28 62 L19 60 L21 34 L2 35 L3 27 L22 25 Z" fill="var(--magenta)"/></svg></span>Affordable tuition &amp;<br>financial assistance<br>programs available</p>
    </div>

    <div class="coverline left" style="left:166px;top:906px">
      <svg class="lead-mark" viewBox="0 0 60 64" aria-hidden="true"><path d="M22 2 L32 2 L30 26 L58 23 L58 32 L30 34 L28 62 L19 60 L21 34 L2 35 L3 27 L22 25 Z" fill="var(--magenta)"/></svg>
      <p class="soft">Miami's premier<br>choice for beauty<br>education</p>
    </div>
  </article>
</body>
</html>
```